Lawn mowing business card design

We need a business card design for our lawn mowing and gardening business which is located in the Northern Beaches of Sydney. Our business name is Meadowline Turf and our logo is predominantly green and yellow in color. Please see our website at www.meadowlineturf.com.au for design ideas. The business targets young professionals and older clientele. As such the font should be easy to read, but I also want the business card to be colorful and stand out.

Target Market(s)

young professionals

Industry/Entity Type

Lawn Care

Contact Information for Business Card

Meadowline Turf, Gareth Pellow, 0478559201, www.meadowlineturf.com.au, email: meadowlineturf@mailbox-example.com

Font styles to use
Serif

Colors
9bcb3b
fbed22

Requirements
Must have
• Must include the details listed above. Must include the attached logo.
Nice to have
• Logo attached with two copies. The logo without any writing is high quality, please feel free to be creative with the text stating our business name "Meadowline Turf" using this file.

```html
<!DOCTYPE html>
<html lang="en">
<head>
<meta charset="utf-8">
<title>Meadowline Turf — Business Card</title>
<link href="https://fonts.googleapis.com/css2?family=Open+Sans:wght@400;600;700&display=swap" rel="stylesheet">
<style>
  :root{
    --backdrop:#777777;
    --paper:#ffffff;
    --leaf:#8dc63f;
    --leaf-deep:#5a8a3c;
    --forest:#1f7a3a;
    --ink:#1b1f2a;
    --sun:#f5c400;
    --soil:#4a3526;
    --grass:#7cc24a;
    --grey-green:#8a9a5b;
  }
  *{margin:0;padding:0;box-sizing:border-box}
  html,body{width:1200px;height:1084px;overflow:hidden;background:var(--backdrop)}
  body{position:relative;font-family:"Open Sans",Arial,sans-serif}

  .card{position:absolute;background:var(--paper);overflow:hidden}
  .card svg.bands{position:absolute;inset:0;width:100%;height:100%}

  /* front */
  .card--front{left:88px;top:116px;width:483px;height:773px}
  .brand-mark{position:absolute;left:40px;top:130px;width:403px;display:flex;align-items:center;justify-content:center;gap:14px}
  .brand-mark__dot{width:34px;height:34px;border-radius:50%;background:var(--leaf)}
  .brand-mark__name{font-size:36px;font-weight:700;color:var(--forest)}
  .holder{position:absolute;left:48px;top:312px;font-size:34px;color:var(--leaf);text-shadow:0 0 6px rgba(0,0,0,.45)}
  .holder b{font-weight:700}
  .holder span{font-weight:400}
  .contact{position:absolute;left:42px;top:0;right:16px;list-style:none}
  .contact li{position:absolute;left:0;display:flex;align-items:center;height:53px;white-space:nowrap}
  .contact .hex{width:53px;height:53px;flex:none}
  .contact .txt{margin-left:12px;font-size:18px;color:#fff;text-shadow:0 0 5px rgba(0,0,0,.7)}

  /* back */
  .card--back{left:643px;top:235px;width:442px;height:771px}
  .badge{position:absolute;left:137px;top:374px;width:176px;height:176px;border-radius:50%;background:var(--paper);box-shadow:0 2px 8px rgba(0,0,0,.45);display:flex;align-items:center;justify-content:center;text-align:center}
  .badge__name{font-size:20px;font-weight:700;color:var(--forest);line-height:1.2}
  .back-title{position:absolute;left:0;width:100%;text-align:center}
  .back-title--name{top:562px;font-size:40px;font-weight:400;color:var(--grey-green);text-shadow:0 0 6px rgba(0,0,0,.35);letter-spacing:.5px}
  .back-title--service{top:621px;font-size:20px;color:#b7b24a;text-shadow:0 0 4px rgba(0,0,0,.3)}
  .back-title--phone{top:660px;font-size:21px;color:var(--sun);text-shadow:0 0 4px rgba(0,0,0,.35)}
  .turf{position:absolute;left:0;bottom:0;width:100%;height:72px}
  .turf__grass{position:absolute;left:0;top:0;width:100%;height:36px;background:linear-gradient(to bottom,#d9efc6,var(--grass))}
  .turf__soil{position:absolute;left:0;bottom:0;width:100%;height:36px;background:var(--soil)}
</style>
</head>
<body>

<section class="card card--front">
  <svg class="bands" viewBox="0 0 403 644" preserveAspectRatio="none" aria-hidden="true">
    <polygon points="270,299 403,279 403,358" fill="var(--leaf)"/>
    <polygon points="270,299 270,350 403,358" fill="var(--leaf-deep)"/>
    <polygon points="0,330 403,358 403,530 0,638" fill="var(--leaf)"/>
  </svg>

  <div class="brand-mark">
    <span class="brand-mark__dot"></span>
    <span class="brand-mark__name">Meadowline Turf</span>
  </div>

  <h1 class="holder"><b>Gareth</b> <span>Pellow</span></h1>

  <ul class="contact">
    <li style="top:437px">
      <svg class="hex" viewBox="0 0 44 44"><polygon points="22,1 41,12 41,32 22,43 3,32 3,12" fill="var(--ink)"/><rect x="17" y="12" width="10" height="19" rx="2" fill="none" stroke="#fff" stroke-width="2"/><circle cx="22" cy="28" r="1" fill="#fff"/></svg>
      <span class="txt">0478 559 201</span>
    </li>
    <li style="top:517px">
      <svg class="hex" viewBox="0 0 44 44"><polygon points="22,1 41,12 41,32 22,43 3,32 3,12" fill="var(--ink)"/><rect x="13" y="16" width="18" height="13" fill="#fff"/><polyline points="13,16 22,23 31,16" fill="none" stroke="var(--ink)" stroke-width="1.6"/></svg>
      <span class="txt">meadowlineturf@mailbox-example.com</span>
    </li>
    <li style="top:597px">
      <svg class="hex" viewBox="0 0 44 44"><polygon points="22,1 41,12 41,32 22,43 3,32 3,12" fill="var(--ink)"/><circle cx="22" cy="22" r="9" fill="none" stroke="#fff" stroke-width="2"/><line x1="13" y1="22" x2="31" y2="22" stroke="#fff" stroke-width="1.5"/><ellipse cx="22" cy="22" rx="4" ry="9" fill="none" stroke="#fff" stroke-width="1.5"/></svg>
      <span class="txt">www.meadowlineturf.com.au</span>
    </li>
  </ul>
</section>

<section class="card card--back">
  <svg class="bands" viewBox="0 0 368 642" preserveAspectRatio="none" aria-hidden="true">
    <polygon points="80,68 288,5 288,104 80,170" fill="var(--leaf-deep)"/>
    <polygon points="80,68 344,112 344,250 80,200" fill="var(--leaf)"/>
    <polygon points="0,222 344,112 344,314" fill="var(--leaf-deep)"/>
    <polygon points="0,222 368,314 368,426 0,426" fill="var(--leaf)"/>
  </svg>

  <div class="badge"><span class="badge__name">Meadowline<br>Turf</span></div>

  <h2 class="back-title back-title--name">MEADOWLINE TURF</h2>
  <p class="back-title back-title--service">Lawn and Garden Maintenance</p>
  <p class="back-title back-title--phone">0478 559 201</p>

  <div class="turf">
    <div class="turf__grass" role="img" aria-label="Strip of grass blades with small daisies"></div>
    <div class="turf__soil"></div>
  </div>
</section>

</body>
</html>
```